Business Card Design for Pastor/Church Leadership - simple, elegant, "different"

Design a name card based on logo and color from our branding guide - see file "MBF Logo and Color".
The teal frame around the logo is not part of the logo and is a not necessary design element for the name card (as the attached PDF file may suggest).
The font suggested by branding is "Frutiger 55 Roman".
The file "not good.pdf", a sample of a name card that is NOT good.
- fonts too small to read
- the tagline on the logo "Still waters, open door" not easy to read with logo used in this design
- "MAPLE GROVE FELLOWSHIP" unnecessarily duplicated - possibly because logo too small
- not sure about the green frame, probably better to drop

Target Market(s)

broad, all people the pastor of an international church in Tokyo meets

Industry/Entity Type

Business

Contact Information for Business Card

Mattias R. Pellworth
Pastor
3-9-4 Kawaranodai, Kaede-ku
Minori 482-0117 (Church)
2-21 Ochibamachi, Kaede-ku
Minori 482-0126 (Home)
Tel: 03-5817-2963
E-mail: pastor@maplegrovefell.org
URL: http://www.maplegrovefell.org

Font styles to use
Sans Serif
Other font styles liked:
• Frutiger 55 Roman (want, not must)

Requirements
Must have
• must include logo
• must make use of the "bright turquoise color"
• Cyan = 59, Magenta = 0, Yellow=24, Black=0
• Red=3.1%, Green=91%, Blue=87.1%
• Key Info (name) must be easy to read (see notes on bad sample namecard attached)

```html
<!DOCTYPE html>
<html lang="en">
<head>
<meta charset="utf-8">
<title>Maple Grove Fellowship – Pastor Business Card</title>
<link rel="stylesheet" href="https://fonts.googleapis.com/css2?family=Source+Sans+3:wght@400;600&display=swap">
<style>
  :root {
    --turquoise: #5bc5c8;
    --ink: #56706b;
    --paper: #ffffff;
    --backdrop: #ffffff;
  }
  * { margin: 0; padding: 0; box-sizing: border-box; }
  html, body {
    width: 1200px;
    height: 1000px;
    overflow: hidden;
    background: var(--backdrop);
    font-family: "Source Sans 3", sans-serif;
  }
  .card {
    position: absolute;
    left: 75px;
    top: 200px;
    width: 1050px;
    height: 600px;
    background: var(--paper);
    overflow: hidden;
  }
  .card__sweep {
    position: absolute;
    inset: 0;
    width: 1050px;
    height: 600px;
  }
  .brand {
    position: absolute;
    left: 65px;
    top: 0;
    width: 476px;
    color: var(--paper);
    text-align: center;
  }
  .brand__mark {
    position: absolute;
    top: 180px;
    left: 0;
    width: 100%;
    font-size: 100px;
    font-weight: 600;
    line-height: 1;
    letter-spacing: 4px;
  }
  .brand__name {
    position: absolute;
    top: 417px;
    left: 0;
    width: 100%;
    font-size: 38px;
    font-weight: 400;
    line-height: 1;
    letter-spacing: -0.2px;
  }
  .brand__rule {
    position: absolute;
    top: 468px;
    left: 20px;
    width: 438px;
    height: 3px;
    background: var(--paper);
  }
  .brand__tagline {
    position: absolute;
    top: 493px;
    left: 0;
    width: 100%;
    font-size: 31px;
    font-weight: 400;
    line-height: 1;
  }
  .contact {
    position: absolute;
    right: 88px;
    top: 0;
    text-align: right;
    white-space: nowrap;
  }
  .contact__name {
    position: absolute;
    right: 0;
    top: 52px;
    font-size: 44px;
    font-weight: 600;
    color: var(--ink);
    line-height: 1;
  }
  .contact__role {
    position: absolute;
    right: 0;
    top: 106px;
    font-size: 35px;
    font-weight: 400;
    color: var(--turquoise);
    line-height: 1;
  }
  .contact__lines {
    position: absolute;
    right: 4px;
    top: 210px;
    list-style: none;
    font-size: 22px;
    color: var(--turquoise);
    line-height: 34px;
  }
  .contact__address {
    position: absolute;
    right: 4px;
    font-size: 18px;
    color: var(--ink);
    line-height: 33px;
    font-style: normal;
  }
  .contact__address--church { top: 385px; }
  .contact__address--home { top: 461px; }
</style>
</head>
<body>
  <article class="card">
    <svg class="card__sweep" viewBox="0 0 1050 600" aria-hidden="true">
      <path d="M0 0 H455 Q560 480 1035 600 H0 Z" fill="var(--turquoise)"/>
    </svg>

    <div class="brand">
      <div class="brand__mark">MBF</div>
      <div class="brand__name">MAPLE GROVE FELLOWSHIP</div>
      <div class="brand__rule"></div>
      <div class="brand__tagline">Still waters, open door</div>
    </div>

    <div class="contact">
      <h1 class="contact__name">Mattias R. Pellworth</h1>
      <p class="contact__role">Pastor</p>
      <ul class="contact__lines">
        <li>03-5817-2963</li>
        <li>pastor@maplegrovefell.org</li>
        <li>www.maplegrovefell.org</li>
      </ul>
      <address class="contact__address contact__address--church">
        3-9-4 Kawaranodai, Kaede-ku<br>Minori 482-0117 (Church)
      </address>
      <address class="contact__address contact__address--home">
        2-21 Ochibamachi, Kaede-ku<br>Minori 482-0126 (Home)
      </address>
    </div>
  </article>
</body>
</html>
```